iOS App Design Project for Pebble Notes

We are looking for a redesign of the UI for our app, Pebble Notes. The app is a to-do list type app with 4 screens, and we already have a UI for it but we would like a nicer looking one that has a better colour scheme and is more intuitive.

We would like something that is a real treat to look at, and that users really want to use. Essentially what we want is the nicest and most simple design possible, as the current UI we have is not very user friendly.

The app is already on the market and is free so if you have an iOS device you can download it and take a look at it, and we have also included screenshots of the app.
Updates

Project Deadline Extended
Reason: I am updating the design brief and will also guarantee the payment.

Target Market(s)

Mobile users looking for simplicity

Requirements
Must have
• - Very visually pleasing
- Simple layout with minimal clutter
- Icons and buttons that explain what they do
Should not have
• Any features that detract from the simplicity of the app are not wanted.

```html
<!DOCTYPE html>
<html lang="en">
<head>
<meta charset="utf-8">
<title>Pebble Notes — Calendar and Task screens</title>
<link rel="stylesheet" href="https://fonts.googleapis.com/css2?family=Arimo:wght@400;700&display=swap">
<style>
  :root {
    --page-bg: #e8ecef;
    --screen-bg: #ffffff;
    --card-top: #ffffff;
    --card-bottom: #ecf3f6;
    --card-border: #b8d2db;
    --row-divider: #9fd0cf;
    --row-text: #4f6570;
    --year-muted: #7a8a92;
    --year-main: #6d7d85;
    --icon-blue: #4d8fc3;
    --tab-label: #4a5c68;
    --heart: #e66f79;
    --dot: #b7bcc0;
    --button-border: #a9c8d4;
    --button-text: #3f5a66;
  }
  * { box-sizing: border-box; margin: 0; padding: 0; }
  html, body {
    width: 1200px;
    height: 1067px;
    overflow: hidden;
    background: var(--page-bg);
    font-family: "Arimo", Arial, sans-serif;
  }
  .canvas { position: relative; width: 1200px; height: 1067px; }
  .screen {
    position: absolute;
    top: 173px;
    width: 320px;
    height: 480px;
    background: var(--screen-bg);
    transform: scale(1.5);
    transform-origin: top left;
    box-shadow: 0 0 2px rgba(0,0,0,0.08);
    overflow: hidden;
  }
  .screen--calendar { left: 80px; }
  .screen--tasks { left: 640px; }

  .year-bar {
    position: absolute; top: 8px; left: 0; width: 320px; height: 24px;
    color: var(--year-muted);
  }
  .year-bar__prev, .year-bar__next {
    position: absolute; top: 8px; font-size: 9px; display: flex; align-items: center; gap: 7px;
  }
  .year-bar__prev { left: 17px; }
  .year-bar__next { right: 17px; }
  .year-bar__current {
    position: absolute; top: 1px; left: 0; width: 100%; text-align: center;
    font-size: 18px; color: var(--year-main);
  }

  .list-card {
    position: absolute; left: 5px; width: 309px;
    display: flex; flex-direction: column;
    background: linear-gradient(180deg, var(--card-top), var(--card-bottom));
    border: 1px solid var(--card-border);
    border-radius: 8px;
    overflow: hidden;
  }
  .list-card--months { top: 35px; height: 382px; }
  .list-card--tasks { top: 5px; height: 365px; }
  .list-row {
    position: relative; flex: 1;
    display: flex; align-items: center;
    font-size: 13px; color: var(--row-text);
    border-bottom: 1px dashed var(--row-divider);
  }
  .list-row:last-child { border-bottom: none; }
  .list-card--months .list-row { padding-left: 34px; }
  .list-card--tasks .list-row { padding-left: 31px; }
  .list-row__dot {
    position: absolute; left: 12px; top: 50%; margin-top: -4px;
    width: 8px; height: 8px; border-radius: 50%; background: var(--dot);
  }
  .list-row__heart { position: absolute; left: 256px; top: 50%; margin-top: -6px; }

  .add-task {
    position: absolute; left: 88px; top: 374px; width: 144px; height: 43px;
    border: 1px solid var(--button-border); border-radius: 7px;
    background: linear-gradient(180deg, #ffffff, #edf3f6);
    box-shadow: 0 2px 3px rgba(80,110,125,0.25);
    font-family: inherit; font-size: 17px; color: var(--button-text);
    display: flex; align-items: center; justify-content: center;
  }

  .tab-bar { position: absolute; left: 0; top: 420px; width: 320px; height: 60px; }
  .tab {
    position: absolute; top: 6px; width: 70px; margin-left: -35px;
    display: flex; flex-direction: column; align-items: center;
    font-size: 12px; color: var(--tab-label);
  }
  .tab svg { display: block; height: 26px; margin-bottom: 3px; }
  .tab--calendar { left: 50px; }
  .tab--task { left: 126px; }
  .tab--notes { left: 200px; }
  .tab--more { left: 281px; }
</style>
</head>
<body>
<main class="canvas">

  <section class="screen screen--calendar" aria-label="Calendar screen">
    <header class="year-bar">
      <span class="year-bar__prev"><span>‹</span><span>2011</span></span>
      <h1 class="year-bar__current" style="font-weight:400">2012</h1>
      <span class="year-bar__next"><span>2013</span><span>›</span></span>
    </header>
    <ul class="list-card list-card--months" style="list-style:none">
      <li class="list-row">December</li>
      <li class="list-row"><span class="list-row__dot"></span>November</li>
      <li class="list-row">October</li>
      <li class="list-row">September</li>
      <li class="list-row">August</li>
      <li class="list-row">July</li>
      <li class="list-row">June</li>
      <li class="list-row">May</li>
      <li class="list-row">April</li>
      <li class="list-row">March</li>
      <li class="list-row">February</li>
      <li class="list-row">January</li>
    </ul>
    <nav class="tab-bar">
      <div class="tab tab--calendar">
        <svg width="22" height="26" viewBox="0 0 22 26"><g fill="var(--icon-blue)"><rect x="1" y="6" width="20" height="3" rx="1"/><rect x="1" y="12" width="20" height="3" rx="1"/><rect x="1" y="18" width="20" height="3" rx="1"/></g></svg>Calendar</div>
      <div class="tab tab--task">
        <svg width="22" height="26" viewBox="0 0 22 26"><path d="M2 14 L8 20 L21 4" fill="none" stroke="var(--icon-blue)" stroke-width="3.5" stroke-linecap="round" stroke-linejoin="round"/></svg>Task</div>
      <div class="tab tab--notes">
        <svg width="24" height="26" viewBox="0 0 24 26"><path d="M14 4 H3 V23 H20 V12" fill="none" stroke="var(--icon-blue)" stroke-width="2"/><path d="M10 16 L11 12 L20 3 L23 6 L14 15 Z" fill="var(--icon-blue)"/></svg>Notes</div>
      <div class="tab tab--more">
        <svg width="26" height="26" viewBox="0 0 26 26"><path d="M13 2 L16.2 9.6 L24.4 10.3 L18.2 15.7 L20.1 23.8 L13 19.5 L5.9 23.8 L7.8 15.7 L1.6 10.3 L9.8 9.6 Z" fill="none" stroke="var(--icon-blue)" stroke-width="2" stroke-linejoin="round"/></svg>More</div>
    </nav>
  </section>

  <section class="screen screen--tasks" aria-label="Task screen">
    <ul class="list-card list-card--tasks" style="list-style:none">
      <li class="list-row">Task 1</li>
      <li class="list-row">Task 2</li>
      <li class="list-row">Task 3</li>
      <li class="list-row">Task 4<svg class="list-row__heart" width="14" height="12" viewBox="0 0 14 12"><path d="M7 11.5 L1.5 6 A3.2 3.2 0 0 1 7 2 A3.2 3.2 0 0 1 12.5 6 Z" fill="var(--heart)"/></svg></li>
      <li class="list-row">Task 5</li>
      <li class="list-row">Task 6<svg class="list-row__heart" width="14" height="12" viewBox="0 0 14 12"><path d="M7 11.5 L1.5 6 A3.2 3.2 0 0 1 7 2 A3.2 3.2 0 0 1 12.5 6 Z" fill="var(--heart)"/></svg></li>
      <li class="list-row">Task 7</li>
      <li class="list-row">Task 9</li>
      <li class="list-row">Task 10</li>
      <li class="list-row">Task 11<svg class="list-row__heart" width="14" height="12" viewBox="0 0 14 12"><path d="M7 11.5 L1.5 6 A3.2 3.2 0 0 1 7 2 A3.2 3.2 0 0 1 12.5 6 Z" fill="var(--heart)"/></svg></li>
      <li class="list-row">Task 12</li>
    </ul>
    <button class="add-task" type="button">Add task</button>
    <nav class="tab-bar">
      <div class="tab tab--calendar">
        <svg width="22" height="26" viewBox="0 0 22 26"><g fill="var(--icon-blue)"><rect x="1" y="6" width="20" height="3" rx="1"/><rect x="1" y="12" width="20" height="3" rx="1"/><rect x="1" y="18" width="20" height="3" rx="1"/></g></svg>Calendar</div>
      <div class="tab tab--task">
        <svg width="22" height="26" viewBox="0 0 22 26"><path d="M2 14 L8 20 L21 4" fill="none" stroke="var(--icon-blue)" stroke-width="3.5" stroke-linecap="round" stroke-linejoin="round"/></svg>Task</div>
      <div class="tab tab--notes">
        <svg width="24" height="26" viewBox="0 0 24 26"><path d="M14 4 H3 V23 H20 V12" fill="none" stroke="var(--icon-blue)" stroke-width="2"/><path d="M10 16 L11 12 L20 3 L23 6 L14 15 Z" fill="var(--icon-blue)"/></svg>Notes</div>
      <div class="tab tab--more">
        <svg width="26" height="26" viewBox="0 0 26 26"><path d="M13 2 L16.2 9.6 L24.4 10.3 L18.2 15.7 L20.1 23.8 L13 19.5 L5.9 23.8 L7.8 15.7 L1.6 10.3 L9.8 9.6 Z" fill="none" stroke="var(--icon-blue)" stroke-width="2" stroke-linejoin="round"/></svg>More</div>
    </nav>
  </section>

</main>
</body>
</html>
```